Wordpress Frontpage/Theme redesign with Female Touch

We’d like to get a new Wordpress theme or childtheme to refresh our beloved website: ladiesinventure.com.au which is a customized version of theme ‘Plume’ that we now find a bit “childish” “chaotic” “unprofessional looking”. We are after a more clear and refined, more professionally looking site.

We’d like to use our current plugins, somebody just needs to redesign the frontpage to give us a new and awesome outlook. We can install and finetune all the necessary plugins.
We know exactly what elements we want to see on the website, see detailed Design requirements. Please also feel free to use any images from http://ladiesinventure.com.au/category/Gallery/ or other stock images.

What we like:
We’d like to have a more professional look, we like ‘news sites’ that: feminine, intelligent, exclusive, smart, elegant, confident aiming towards the higher end of the female entrepreneur market. Websites like:
http://www.gardenmorrow.com/
http://www.velvora.com/velvora/
http://thelattice.quorvix.com.au/
http://brightpeltavo.com/
http://layoutmarket.net/item/pagevane-flat-magazine-theme-/full_screen_preview/4917362

Project Deadline Extended
Reason: Hi guys, We are extending the deadline of the project as we are still waiting for the perfect design. Good luck everyone! Cheers

Target Market(s)

Australian national community of like-minded aspiring and accomplished female entrepreneurs. Age women in their 30’s and 40’s – typically confident and established powerful and driven, passionate women.

Requirements
Must have
• Detailed Design Requirements
• Read together with “Ladies in Venture website screenshot with numbers.jpg”:
• 1. Logo: New Logo provided + we need the tagline with nice characters
• 2. Social Media Buttons should be in the Footer: Chirplet, Kinfold, Pinboardly, Workcircle, Feed
• 3. Drop down Menu (Multi level) JOIN menu highlighted
• 4. Picture slideshow where we can put our photos, adds, event pictures, happy women faces etc.
• 5. Search with Search button
• 6. Space which is easy to edit and where we can quickly write news, or important information
• 7. Widget: News Letter Signup (Should be highlighted and well visible)
• 8. Widget: Login with standard Kinfold login button (Unikey plugin) this can be at top row header
• 9. Widget: Question of the week, Online poll
• 10. Widget: Upcoming events, Gatherly widget
• 11. Featured Video Display: 2 videos which are in the “featured videos” category, (photo + excerpt)
• 12. Featured Blog Display: Displaying blog entries which are in the “featured blogs” category (photo + excerpt)
• 13. Widgets Standard Wordpress widgets to show recent activities (can be different)
• 14. Same as 13.
• 15. Same as 13.
• 16. Same as 13.
• 17. Kinfold News Feed
• 18. Footer: Social media buttons see no.2., + credit, etc..
• .
• + New features we need:
• 19. Featured members (displaying Level2 users from Q7 Roster Plugin)
• 20. Promo Viddora Video: fix space on the top somewhere, picture provided.
• 21. Place for advertisements
• Other requirements:
• • Speed: Please don’t create huge background images/javascript files, current Frontpage is ~600KB.
• • Security: no hidden codes, no well known vulnerabilities.
• • Compatibility: please use standard Wordpress features. Later on we want to add more features like: Webshop, Palpanel
• • Resizable: When we change window size, or see it on mobile, it rearranges itself.

```html
<!DOCTYPE html>
<html lang="en">
<head>
<meta charset="utf-8">
<title>Ladies in Venture</title>
<link rel="stylesheet" href="https://fonts.googleapis.com/css2?family=Amaranth:ital,wght@0,400;0,700;1,400;1,700&family=Arimo:wght@400;700&family=Open+Sans:ital,wght@0,400;0,600;0,700;1,400;1,600&display=swap">
<style>
:root{
  --pink:#e2155f;
  --orange:#f7901e;
  --steel:#4b7898;
  --nav:#4b4b4b;
  --nav-line:#5e5e5e;
  --text:#333;
  --muted:#666;
  --rule:#dcdcdc;
  --page-bg:#efefef;
  --panel:#f5f5f5;
  --social-blue:#3b5998;
  --footer:#d7d7d7;
}
*{box-sizing:border-box;margin:0;padding:0}
html,body{width:1200px;height:3046px;overflow:hidden}
body{background:var(--page-bg);font-family:"Open Sans",Arial,sans-serif;color:var(--text);position:relative}
.page{position:absolute;left:126px;top:0;width:948px;height:3046px;background:#fff}
.abs{position:absolute}
a{color:inherit;text-decoration:none}

/* header */
.brand{left:144px;top:18px;display:flex;align-items:center;gap:12px}
.brand-mark{width:46px;height:46px;background:var(--pink)}
.brand-name{font-family:"Arimo",Arial,sans-serif;font-size:35px;color:var(--steel);font-weight:400;letter-spacing:-.3px}
.connect{left:857px;top:15px;width:197px;height:28px;background:var(--social-blue);border-radius:4px;color:#fff;font-size:11px;font-weight:600;display:flex;align-items:center;padding-left:14px;gap:8px}
.connect .dot{width:14px;height:14px;background:#fff;opacity:.85}
.search{left:857px;top:51px;width:197px;height:27px;display:flex}
.search span{flex:1;background:#d9d9d9;font-size:12px;font-style:italic;color:#555;padding:5px 8px}
.search button{width:29px;border:0;background:var(--orange);display:flex;align-items:center;justify-content:center}

/* nav */
.main-nav{left:144px;top:93px;width:912px;height:45px;background:var(--nav);display:flex}
.main-nav a{position:relative;display:flex;align-items:center;justify-content:center;font-family:"Amaranth",sans-serif;font-style:italic;font-size:19px;color:#c8c8c8;border-right:1px solid var(--nav-line)}
.main-nav a.on{background:var(--orange);color:#fff}
.main-nav a.join{background:var(--pink);color:#fff;border:0}
.main-nav a.sub::after{content:"";position:absolute;bottom:4px;left:50%;margin-left:-5px;border:5px solid transparent;border-top-color:#bbb;border-bottom:0}

/* hero */
.hero{left:144px;top:138px;width:912px;height:368px;background:linear-gradient(100deg,#dcdcdc 0%,#c9c6c4 35%,#a8a3a0 55%,#55504e 75%,#2b2928 100%)}
.hero h1{position:absolute;left:24px;top:104px;font-family:"Amaranth",sans-serif;font-weight:700;font-size:42px;line-height:48px;color:var(--pink)}

/* welcome */
.welcome{left:144px;top:524px;width:599px}
.welcome h2{font-family:"Amaranth",sans-serif;font-weight:400;font-size:22px;color:var(--pink);border-bottom:1px solid var(--rule);padding-bottom:4px;position:relative}
.welcome h2::after{content:"";position:absolute;left:0;bottom:-1px;width:160px;height:2px;background:var(--pink)}
.welcome p{font-family:"Arimo",sans-serif;font-size:11.5px;color:#444;margin-top:8px;letter-spacing:-.1px;text-transform:uppercase}
.welcome .motto{font-family:"Amaranth",sans-serif;font-size:20px;color:var(--pink);margin-top:4px;text-transform:none;letter-spacing:0}

/* section heads */
.sec-head{left:144px;width:599px;height:38px;border-bottom:3px solid var(--orange)}
.sec-head h2{display:inline-block;height:38px;line-height:38px;background:var(--pink);color:#fff;font-family:"Amaranth",sans-serif;font-weight:400;font-size:20px;padding:0 18px}
.sec-head .more{position:absolute;right:0;bottom:3px;width:28px;height:28px;background:var(--orange);display:flex;align-items:center;justify-content:center}

/* lead story */
.lead{left:144px;width:280px}
.lead .photo{height:152px}
.lead h3{font-size:13px;font-weight:400;color:var(--pink);margin-top:18px}
.lead .role{font-size:11.5px;font-weight:600;color:#222;margin-top:2px}
.lead .date{font-size:11px;font-style:italic;color:#333;margin-top:8px;display:flex;gap:14px;align-items:center}
.lead p{font-size:11px;line-height:17px;color:#555;margin-top:8px}
.read-more{display:block;margin:6px 0 0 auto;width:75px;height:20px;background:var(--orange);color:#fff;font-size:10px;font-weight:700;font-style:italic;text-align:center;line-height:20px}

/* side lists */
.mini-list{left:445px;width:298px;list-style:none}
.mini-list li{display:flex;gap:10px;height:63px}
.mini-list .thumb{width:49px;height:49px;flex:none}
.mini-list b{display:block;font-size:12.5px;font-weight:700;color:#222;line-height:16px}
.mini-list .name{display:block;font-size:13px;color:var(--pink);line-height:16px}
.mini-list .role{display:block;font-size:11.5px;font-weight:600;color:#222;line-height:16px}
.mini-list .when{display:block;font-size:11.5px;color:#444;line-height:16px}

/* videos */
.video{width:290px}
.video .frame{height:171px;position:relative}
.video .play{position:absolute;left:50%;top:50%;margin:-20px 0 0 -24px;width:48px;height:40px;background:var(--pink);display:flex;align-items:center;justify-content:center}
.video h3{font-size:13.5px;font-weight:400;color:var(--pink);margin-top:10px}
.video .by{font-size:11px;font-style:italic;color:#333;margin-top:2px}
.video p{font-size:11.5px;line-height:16px;color:#555;text-align:justify;margin-top:4px}

/* social feed */
.feed{left:144px;top:2227px;width:599px;height:741px;border:1px solid #cfcfcf;background:#fff}
.feed-top{display:flex;justify-content:space-between;align-items:center;padding:14px 16px 12px;border-bottom:1px solid #e4e4e4}
.feed-top .name{font-family:"Arimo",sans-serif;font-size:26px;color:var(--steel)}
.likebox{display:flex;gap:8px;align-items:flex-start;font-size:10px;color:#444;width:160px}
.likebox .btn{border:1px solid #c4cde0;background:#eef1f7;padding:1px 6px;color:var(--social-blue);font-weight:600}
.post-avatar{left:14px;top:76px;width:40px;height:40px}
.post{left:88px;top:88px;width:474px}
.post .shot{height:275px}
.post .acts{display:flex;gap:22px;font-size:11px;font-weight:600;color:#333;padding:10px 4px 8px;border-bottom:1px solid #e4e4e4}
.post .acts span{font-weight:400}
.post .caption{font-size:11px;color:#666;padding:6px 4px;line-height:15px}
.post .reply{display:flex;gap:8px;padding:4px}
.post .reply i{width:24px;height:24px;background:#7e6f6a;flex:none}
.post .reply span{flex:1;border:1px solid #ccc;font-size:10px;color:#999;padding:4px 6px}
.scroll{left:575px;top:88px;width:4px;height:300px;background:#f2c2d3}
.scroll::before{content:"";position:absolute;left:0;top:0;width:4px;height:30px;background:var(--pink)}
.fans{left:10px;top:502px;width:569px;height:214px;border-top:1px solid #e4e4e4}
.fans-grid{position:absolute;left:0;top:12px;width:569px;height:200px;background:linear-gradient(90deg,#6a5a55,#a89488,#4f4a58,#b49a8e,#5f5a62)}
.plugin-note{left:14px;top:722px;font-size:9px;color:#777}

/* widgets */
.widget{left:771px;width:285px;border:1px solid #e1e1e1;background:#fff}
.widget h3{height:36px;line-height:36px;background:var(--pink);color:#fff;font-family:"Amaranth",sans-serif;font-style:italic;font-weight:400;font-size:19px;padding-left:14px}
.view-all{position:absolute;right:14px;bottom:8px;width:60px;height:17px;background:var(--pink);color:#fff;font-size:9.5px;font-weight:700;font-style:italic;text-align:center;line-height:17px;clip-path:polygon(8px 0,100% 0,100% 100%,0 100%)}

.newsletter{top:538px;height:195px;background:var(--panel)}
.newsletter form{padding:16px 18px 0 20px}
.field{display:flex;align-items:center;margin-bottom:14px}
.field label{width:46px;font-size:12px;font-style:italic;font-weight:600;color:#333}
.field span{flex:1;height:28px;border:1px solid #ccc;background:#fff}
.subscribe{display:block;margin:22px auto 0;width:140px;height:25px;border:0;background:var(--pink);color:#fff;font-weight:700;font-size:13px;clip-path:polygon(12px 0,calc(100% - 12px) 0,100% 100%,0 100%)}

.poll{top:761px;height:268px}
.poll h4{font-size:13px;font-weight:700;color:var(--pink);text-decoration:underline;margin:14px 0 8px 20px}
.poll ul{list-style:none;padding:0 16px 0 18px}
.poll li{display:flex;gap:10px;font-size:11.5px;line-height:15px;color:#333;margin-bottom:12px}
.poll li i{width:13px;height:13px;flex:none;margin-top:2px;background:#f6d33c;border:1px solid #b99a1c;transform:rotate(45deg) scale(.85)}
.poll-actions{position:absolute;left:0;bottom:0;width:100%;height:24px;display:flex;gap:2px}
.poll-actions span{flex:1;background:var(--pink);color:#fff;font-size:11px;font-weight:700;font-style:italic;text-align:center;line-height:24px}
.poll-actions span.vote{background:var(--orange)}

.events{top:1062px;height:329px}
.event{display:flex;gap:12px;margin:18px 14px 0;border:1px solid #ddd;background:#fafafa;height:67px;padding:6px 8px}
.cal{width:59px;height:54px;border:1px solid #c9c9c9;background:#fff;text-align:center;position:relative;flex:none}
.cal::before{content:"";position:absolute;left:0;top:0;width:100%;height:8px;background:#d6d6d6}
.cal b{display:block;font-size:22px;color:var(--pink);line-height:26px;margin-top:10px}
.cal small{display:block;font-size:8px;color:#555}
.event .t{font-size:13.5px;color:var(--pink);line-height:17px}
.event .tm{font-size:11.5px;font-weight:700;font-style:italic;color:#333;display:flex;gap:5px;align-items:center}
.event .x{font-size:11px;color:var(--orange)}

.recent{top:1417px;height:325px}
.post-list{list-style:none;padding:14px 12px 0}
.post-list li{display:flex;gap:10px;height:63px;border-bottom:1px solid #ececec;padding-top:4px}
.post-list .thumb{width:49px;height:49px;flex:none}
.post-list .name{display:block;font-size:13px;color:var(--pink);line-height:16px}
.post-list .role{display:block;font-size:11px;font-weight:600;color:#222;line-height:15px}
.post-list .when{display:block;font-size:11px;color:#444;line-height:15px}

.link-list{list-style:none;padding-top:6px}
.link-list li{height:26.5px;line-height:26px;font-size:11.5px;color:#444;padding-left:12px;border-bottom:1px solid #e9e9e9;display:flex;gap:6px;align-items:center}
.link-list li::before{content:"»";color:#777}
.link-list li.on{background:var(--orange);color:#fff;border-color:var(--orange)}
.link-list li.on::before{color:#fff}
.archives{top:1772px;height:353px}
.categories{top:2158px;height:353px}

.comments{top:2542px;height:422px}
.comment-list{list-style:none;padding:8px 14px 0}
.comment-list li{border-bottom:1px solid #e9e9e9;padding:6px 0 8px;font-size:12px;line-height:16px;color:#222}
.comment-list li a{color:var(--pink)}
.comment-list li em{display:block;font-size:10.5px;color:#444}

/* footer */
.site-footer{left:126px;top:2984px;width:948px;height:62px;background:var(--footer)}
.foot-links{position:absolute;left:18px;top:10px;font-size:11.5px;color:#555}
.foot-links a:first-child{color:var(--pink)}
.credit{position:absolute;left:18px;top:30px;font-size:11.5px;color:#444}
.social{position:absolute;left:743px;top:12px;display:flex;gap:8px;list-style:none}
.social li{width:30px;height:30px;border-radius:50%;background:#5c5c5c;border:2px solid #fff;box-shadow:0 0 0 1px #999}
</style>
</head>
<body>
<div class="page"></div>

<header>
  <div class="abs brand"><span class="brand-mark"></span><span class="brand-name">Ladies in Venture</span></div>
  <a class="abs connect" href="#"><span class="dot"></span>Connect with Kinfold</a>
  <form class="abs search"><span>Search for:</span><button type="button" aria-label="Search"><svg width="14" height="14" viewBox="0 0 14 14"><circle cx="6" cy="6" r="4.2" fill="none" stroke="#fff" stroke-width="2"/><path d="M9 9l4 4" stroke="#fff" stroke-width="2.2"/></svg></button></form>
  <nav class="abs main-nav">
    <a class="on" href="#" style="width:116px">Home</a>
    <a class="sub" href="#" style="width:122px">About</a>
    <a class="sub" href="#" style="width:123px">Events</a>
    <a class="sub" href="#" style="width:179px">Biz Directory</a>
    <a href="#" style="width:126px">Partners</a>
    <a href="#" style="width:142px">Contact</a>
    <a class="join" href="#" style="width:104px">Join</a>
  </nav>
</header>

<section class="abs hero" role="img" aria-label="Slideshow photo: a woman speaking at a microphone on stage">
  <h1>Australia's No. 1<br>organisation for<br>female entrepreneurs</h1>
</section>

<section class="abs welcome">
  <h2>Welcome to Ladies in Venture</h2>
  <p>We provide women entrepreneurs with information, support and a community in Australia</p>
  <p class="motto">do what you love • inspire others • change the world</p>
</section>

<!-- Top News -->
<div class="abs sec-head" style="top:648px"><h2>Top News</h2><span class="more"><svg width="14" height="14"><path d="M7 1v12M1 7h12" stroke="#fff" stroke-width="2.5"/></svg></span></div>
<article class="abs lead" style="top:698px">
  <div class="photo" role="img" aria-label="Group photo of smiling members at an event" style="background:linear-gradient(90deg,#5a3a34,#b67a6a,#7b5a55,#c79a86)"></div>
  <h3>This happens when you get over your</h3>
  <div class="date">December 4th, 2013 <span><svg width="12" height="8" viewBox="0 0 12 8"><ellipse cx="6" cy="4" rx="5.5" ry="3.5" fill="none" stroke="#333"/><circle cx="6" cy="4" r="1.6" fill="#333"/></svg> 23 Views</span></div>
  <p>Lorem ipsum dolor sit amet, consectetur adipiscing elit. Integer lobortis orci nibh, id blandit urna porta ....</p>
  <a class="read-more" href="#">Read more</a>
</article>
<ul class="abs mini-list" style="top:698px">
  <li><span class="thumb" role="img" aria-label="Portrait thumbnail" style="background:#8a6a5e"></span><div><b>This happens when you get over...</b><span class="when">December 4th, 2013</span></div></li>
  <li><span class="thumb" role="img" aria-label="Portrait thumbnail" style="background:#6e5a52"></span><div><b>This happens when you get over...</b><span class="when">December 4th, 2013</span></div></li>
  <li><span class="thumb" role="img" aria-label="Portrait thumbnail" style="background:#a07a6a"></span><div><b>This happens when you get over...</b><span class="when">December 4th, 2013</span></div></li>
  <li><span class="thumb" role="img" aria-label="Portrait thumbnail" style="background:#9a6e52"></span><div><b>This happens when you get over...</b><span class="when">December 4th, 2013</span></div></li>
  <li><span class="thumb" role="img" aria-label="Portrait thumbnail" style="background:#7a6660"></span><div><b>This happens when you get over...</b><span class="when">December 4th, 2013</span></div></li>
</ul>

<!-- Featured Articles -->
<div class="abs sec-head" style="top:1032px"><h2>Featured Articles</h2><span class="more"><svg width="14" height="14"><path d="M7 1v12M1 7h12" stroke="#fff" stroke-width="2.5"/></svg></span></div>
<article class="abs lead" style="top:1082px">
  <div class="photo" role="img" aria-label="Portrait of a businesswoman in red" style="height:156px;background:linear-gradient(90deg,#e8e2df,#c2866f,#d9b6a8)"></div>
  <h3>Marisa D'Elton</h3>
  <div class="role">Her International and CEO of Goldleaf Gals</div>
  <div class="date">August 13th, 2013</div>
  <p>So you need to cold call to build your client base but you continually have a BLOCK...</p>
  <a class="read-more" href="#">Read more</a>
</article>
<ul class="abs mini-list" style="top:1082px">
  <li><span class="thumb" role="img" aria-label="Portrait thumbnail" style="background:#c0604f"></span><div><span class="name">Marisa D'Elton</span><span class="role">Her International and CEO of Goldleaf</span><span class="when">December 4th, 2013</span></div></li>
  <li><span class="thumb" role="img" aria-label="Portrait thumbnail" style="background:#5a5250"></span><div><span class="name">Clara Novak,</span><span class="role">Specialises in Personal Development</span><span class="when">December 4th, 2013</span></div></li>
  <li><span class="thumb" role="img" aria-label="Portrait thumbnail" style="background:#b08a74"></span><div><span class="name">Jess Armitage</span><span class="role">Her The Press Duchess</span><span class="when">December 4th, 2013</span></div></li>
  <li><span class="thumb" role="img" aria-label="Portrait thumbnail" style="background:#8c6e5e"></span><div><span class="name">Tara Bellamy</span><span class="role">Her Launch Savvy</span><span class="when">December 4th, 2013</span></div></li>
  <li><span class="thumb" role="img" aria-label="Portrait thumbnail" style="background:#6e5046"></span><div><span class="name">Ruby Hartnell</span><span class="role">Director of Tailorline Communications</span><span class="when">December 4th, 2013</span></div></li>
</ul>

<!-- Featured Blog -->
<div class="abs sec-head" style="top:1416px"><h2>Featured Blog</h2><span class="more"><svg width="14" height="14"><path d="M7 1v12M1 7h12" stroke="#fff" stroke-width="2.5"/></svg></span></div>
<article class="abs lead" style="top:1468px">
  <div class="photo" role="img" aria-label="Black and white portrait of a woman" style="height:156px;background:linear-gradient(90deg,#f0f0f0,#9a9a9a,#3c3c3c,#d0d0d0)"></div>
  <h3>Clara Novak</h3>
  <div class="role">Specialises in Personal Development</div>
  <div class="date">June 10th, 2013</div>
  <p>So you need to cold call to build your client base but you continually have a BLOCK...</p>
  <a class="read-more" href="#">Read more</a>
</article>
<ul class="abs mini-list" style="top:1468px">
  <li><span class="thumb" role="img" aria-label="Portrait thumbnail" style="background:#5a5250"></span><div><span class="name">Clara Novak</span><span class="role">Specialises in Personal Development</span><span class="when">June 10th, 2013</span></div></li>
  <li><span class="thumb" role="img" aria-label="Portrait thumbnail" style="background:#a58470"></span><div><span class="name">Leona Whitfield</span><span class="role">CEO of Finer Every Day</span><span class="when">July 1st, 2013</span></div></li>
  <li><span class="thumb" role="img" aria-label="Portrait thumbnail" style="background:#6a5048"></span><div><span class="name">Samira Oduya</span><span class="role">CEO of Rising Woman</span><span class="when">July 1st, 2013</span></div></li>
  <li><span class="thumb" role="img" aria-label="Portrait thumbnail" style="background:#8c6e5e"></span><div><span class="name">Priya Ranasuriya</span><span class="role">Her Launch Savvy</span><span class="when">December 4th, 2013</span></div></li>
  <li><span class="thumb" role="img" aria-label="Portrait thumbnail" style="background:#6e5046"></span><div><span class="name">Ruby Hartnell</span><span class="role">Managing Director of The CANDID Team</span><span class="when">July 13st, 2013</span></div></li>
</ul>

<!-- Featured videos -->
<div class="abs sec-head" style="top:1799px"><h2>featured videos</h2><span class="more"><svg width="14" height="14"><path d="M7 1v12M1 7h12" stroke="#fff" stroke-width="2.5"/></svg></span></div>
<article class="abs video" style="left:144px;top:1851px">
  <div class="frame" role="img" aria-label="Video still: audience seated at a community event" style="background:linear-gradient(180deg,#8a9aa8,#6a5a52 60%,#3e3430)"><span class="play"><svg width="16" height="18"><path d="M1 1l14 8-14 8z" fill="#fff"/></svg></span></div>
  <h3>Ladies in Venture Testimonial</h3>
  <div class="by">Eszter Vadas, March 6, 2013</div>
  <p>Ladies in Venture (LV) is the No.1. community for Australian female entrepreneurs, run by Eszter Vadas and focuses on empowerment of women and equal opportunity advocacy.</p>
</article>
<article class="abs video" style="left:453px;top:1851px">
  <div class="frame" role="img" aria-label="Video still: women in conversation at an interview" style="background:linear-gradient(180deg,#7a6a5e,#4e423c 60%,#2e2824)"><span class="play"><svg width="16" height="18"><path d="M1 1l14 8-14 8z" fill="#fff"/></svg></span></div>
  <h3>Melbourne Interviews Part 3 3/3</h3>
  <div class="by">Eszter Vadas, January 11, 2013</div>
  <p>This video is part 3 of a series of 3 videos discussing the advantages of being a woman in startup land, the importance of mentorship and helping other women in business.</p>
</article>

<!-- Kinfold news -->
<div class="abs sec-head" style="top:2173px"><h2>Kinfold news</h2></div>
<section class="abs feed">
  <div class="feed-top">
    <span class="name">Ladies in Venture</span>
    <div class="likebox"><span class="btn">Like</span><span>You like this.<br>60,520 people like this</span></div>
  </div>
  <div class="abs post-avatar" role="img" aria-label="Page avatar" style="background:#8a7068"></div>
  <div class="abs scroll"></div>
  <div class="abs post">
    <div class="shot" role="img" aria-label="Quote card with a portrait of a smiling founder" style="background:linear-gradient(90deg,#2a2a2a 0%,#3a3a3a 45%,#c9a98a 70%,#7a2a3a 100%)"></div>
    <div class="acts"><b>Like</b><b>Comment</b><b>Share</b><span>November 28 at 7:55pm</span></div>
    <p class="caption">Are you having a gorgeous Thursday? Share your biggest achievement of the week with us below. We'd love to hear about it!</p>
    <div class="reply"><i></i><span>Write a comment...</span></div>
  </div>
  <div class="abs fans"><div class="fans-grid" role="img" aria-label="Grid of follower profile pictures"></div></div>
  <div class="abs plugin-note">Kinfold social plugin</div>
</section>

<!-- Sidebar -->
<aside>
  <section class="abs widget newsletter">
    <h3>Sing up for our newsletter!</h3>
    <form>
      <div class="field"><label>Name:</label><span></span></div>
      <div class="field"><label>Email:</label><span></span></div>
      <button class="subscribe" type="button">Subscribe</button>
    </form>
  </section>

  <section class="abs widget poll">
    <h3>Question of the week:</h3>
    <h4>Are You Selling Overseas?</h4>
    <ul>
      <li><i></i>Yes, in fact most of my sales come from overseas</li>
      <li><i></i>Yes, I can say I have made a few sales overseas</li>
      <li><i></i>No, I don't and not planning to</li>
      <li><i></i>No I don't, but considering entering overseas markets</li>
    </ul>
    <div class="poll-actions"><span class="vote">Vote</span><span>View Results</span><span>Polls Archive</span></div>
  </section>

  <section class="abs widget events">
    <h3>Upcoming Events</h3>
    <div class="event"><div class="cal"><b>25</b><small>Dec 2013</small></div><div><div class="t">Lorem ipsum dolor sit</div><div class="tm"><svg width="11" height="11"><circle cx="5.5" cy="5.5" r="4.5" fill="none" stroke="#333" stroke-width="1.4"/><path d="M5.5 3v3h2" stroke="#333" fill="none" stroke-width="1.2"/></svg>11:00 PM to 7 : 00 pm</div><div class="x">consectetur adipiscing elit.</div></div></div>
    <div class="event"><div class="cal"><b>25</b><small>Dec 2013</small></div><div><div class="t">Lorem ipsum dolor sit</div><div class="tm"><svg width="11" height="11"><circle cx="5.5" cy="5.5" r="4.5" fill="none" stroke="#333" stroke-width="1.4"/><path d="M5.5 3v3h2" stroke="#333" fill="none" stroke-width="1.2"/></svg>11:00 PM to 7 : 00 pm</div><div class="x">consectetur adipiscing elit.</div></div></div>
    <div class="event"><div class="cal"><b>25</b><small>Dec 2013</small></div><div><div class="t">Lorem ipsum dolor sit</div><div class="tm"><svg width="11" height="11"><circle cx="5.5" cy="5.5" r="4.5" fill="none" stroke="#333" stroke-width="1.4"/><path d="M5.5 3v3h2" stroke="#333" fill="none" stroke-width="1.2"/></svg>11:00 PM to 7 : 00 pm</div><div class="x">consectetur adipiscing elit.</div></div></div>
    <a class="view-all" href="#">View All</a>
  </section>

  <section class="abs widget recent">
    <h3>Recent Posts</h3>
    <ul class="post-list">
      <li><span class="thumb" role="img" aria-label="Portrait thumbnail" style="background:#5a5250"></span><div><span class="name">Clara Novak</span><span class="role">Specialises in Personal Development</span><span class="when">June 10th, 2013</span></div></li>
      <li><span class="thumb" role="img" aria-label="Portrait thumbnail" style="background:#a58470"></span><div><span class="name">Leona Whitfield</span><span class="role">CEO of Finer Every Day</span><span class="when">July 1st, 2013</span></div></li>
      <li><span class="thumb" role="img" aria-label="Portrait thumbnail" style="background:#6a5048"></span><div><span class="name">Samira Oduya</span><span class="role">CEO of Rising Woman</span><span class="when">July 1st, 2013</span></div></li>
      <li><span class="thumb" role="img" aria-label="Portrait thumbnail" style="background:#8c6e5e"></span><div><span class="name">Priya Ranasuriya</span><span class="role">Her Launch Savvy</span><span class="when">December 4th, 2013</span></div></li>
    </ul>
    <a class="view-all" href="#">View All</a>
  </section>

  <section class="abs widget archives">
    <h3>Archives</h3>
    <ul class="link-list">
      <li class="on">November 2013</li><li>October 2013</li><li>September 2013</li><li>August 2013</li><li>July 2013</li><li>June 2013</li><li>May 2013</li><li>April 2013</li><li>March 2013</li><li>February 2013</li><li>January 2013</li>
    </ul>
    <a class="view-all" href="#">View All</a>
  </section>

  <section class="abs widget categories">
    <h3>Categories</h3>
    <ul class="link-list">
      <li class="on">Article (48)</li><li>Empowerment of Women (2)</li><li>Featured Article (6)</li><li>Featured Video (2)</li><li>female empowerment (3)</li><li>Gallery (12)</li><li>Guest Blog (8)</li><li>Interview (5)</li><li>News (1)</li><li>Video (7)</li><li>Video Interview (23)</li>
    </ul>
    <a class="view-all" href="#">View All</a>
  </section>

  <section class="abs widget comments">
    <h3>Recent Comments</h3>
    <ul class="comment-list">
      <li>Nadia Forsythe on <a href="#">Community Support</a><em>November 12th, 2013 at 19:59</em></li>
      <li>Joy Pembleton on <a href="#">Migrant entrepreneurs overcome barriers to starting up businesses in Australia</a><em>November 12th, 2013 at 19:59</em></li>
      <li>Tess on <a href="#">Get up offa that thing Motivation #1</a><em>November 12th, 2013 at 19:59</em></li>
      <li>Anahera Tawhiri on <a href="#">Cold Calling: 3 tips to get past the Gate Keeper</a><em>November 12th, 2013 at 19:59</em></li>
      <li>Greta Falkner on <a href="#">The key to being a successful entrepreneur</a><em>November 12th, 2013 at 19:59</em></li>
    </ul>
    <a class="view-all" href="#">View All</a>
  </section>
</aside>

<footer class="abs site-footer">
  <div class="foot-links"><a href="#">Home</a> / <a href="#">About</a> / <a href="#">Events</a> / <a href="#">Biz Directory</a> / <a href="#">Partners</a> / <a href="#">Contact</a> / <a href="#">Join</a></div>
  <div class="credit">Ladies in Venture 2013. All rights reserved</div>
  <ul class="social">
    <li aria-label="Kinfold"></li><li aria-label="Chirplet"></li><li aria-label="Workcircle"></li><li aria-label="Feed"></li><li aria-label="Pinboardly"></li>
  </ul>
</footer>
</body>
</html>
```